IT Consulting Business needs a web design

We need a web design for an IT Consulting company called "Vorenix". We want to replace the existing web site (www.vorenix-example.com) with a new design. Our services are IT Consulting, IT Training, IT Outsourcing.
We would like to see designs that communicate "Trusted IT Advisor" with modern & bold design.

We would like to see the design of 2 pages:
1. Home page (www.vorenix-example.com)
2. The detail page (http://www.vorenix-example.com/index_files/consulting.htm)

Industry/Entity Type

Business

```html
<!DOCTYPE html>
<html lang="en">
<head>
<meta charset="utf-8">
<title>Vorenix — IT Consulting</title>
<link href="https://fonts.googleapis.com/css2?family=PT+Sans:ital,wght@0,400;0,700;1,400;1,700&family=Arimo:wght@400&display=swap" rel="stylesheet">
<style>
  :root {
    --bg: #ececec;
    --page: #ffffff;
    --brand: #1253b3;
    --icon: #2d64c3;
    --ink: #6b6b6b;
    --ink-soft: #7a7a7a;
    --nav-top: #b9b9bb;
    --nav-bottom: #88898c;
    --red-top: #f2262a;
    --red-bottom: #c40408;
    --band: #f3f3f3;
  }
  * { margin: 0; padding: 0; box-sizing: border-box; }
  html, body { width: 1200px; height: 900px; overflow: hidden; }
  body { background: var(--bg); font-family: "Arimo", Arial, sans-serif; position: relative; }
  .page { position: absolute; left: 24px; top: 0; width: 1146px; height: 900px; background: var(--page); }
  .abs { position: absolute; }

  .logo { left: 100px; top: 30px; font-family: "PT Sans", sans-serif; font-weight: 700; font-size: 42px; color: var(--brand); letter-spacing: 0.5px; }

  .contact { top: 11px; font-family: "PT Sans", sans-serif; font-style: italic; font-size: 14px; color: var(--ink); display: flex; align-items: center; gap: 6px; }
  .contact svg { fill: #9a9a9a; }
  .contact-phone { left: 835px; }
  .contact-mail { left: 968px; }

  .nav { left: 429px; top: 43px; width: 681px; height: 39px; background: linear-gradient(var(--nav-top), var(--nav-bottom)); border-radius: 3px; display: flex; box-shadow: 0 8px 8px -6px rgba(0,0,0,.35); }
  .nav a { color: #fff; text-decoration: none; font-size: 14px; display: flex; align-items: center; justify-content: center; height: 39px; }
  .nav a.active { background: var(--brand); border-radius: 3px 0 0 3px; width: 77px; position: relative; }
  .nav a.active::after { content: ""; position: absolute; bottom: -5px; left: 34px; border: 5px solid transparent; border-bottom: 0; border-top-color: var(--brand); }

  .hero { left: 86px; top: 107px; width: 1025px; height: 416px; background: linear-gradient(100deg, #e9ecef 0%, #f5f5f5 25%, #3a3c44 42%, #eaeaea 55%, #c9c0b6 75%, #e2e6da 100%); box-shadow: -6px 0 14px -6px rgba(0,0,0,.3), 6px 0 14px -6px rgba(0,0,0,.3); }
  .hero-shadow { top: 522px; width: 430px; height: 30px; background: radial-gradient(ellipse at top, rgba(0,0,0,.35), transparent 70%); }
  .tagline { left: 643px; top: 230px; font-family: "PT Sans", sans-serif; font-style: italic; font-size: 29px; color: #7b7b7b; display: flex; align-items: center; gap: 2px; }
  .tagline span.rule { width: 30px; height: 1px; background: #7b7b7b; }
  .btn { left: 759px; top: 300px; width: 169px; height: 39px; border-radius: 6px; background: linear-gradient(var(--red-top), var(--red-bottom)); color: #fff; font-family: "PT Sans", sans-serif; font-size: 21px; display: flex; align-items: center; justify-content: center; letter-spacing: .5px; box-shadow: 0 2px 3px rgba(0,0,0,.25); }

  .section-title { left: 0; width: 1150px; top: 582px; display: flex; justify-content: center; align-items: center; gap: 26px; font-family: "PT Sans", sans-serif; font-style: italic; font-size: 29px; color: var(--ink); }
  .section-title .rule { width: 56px; height: 1px; background: #8a8a8a; }

  .value { top: 652px; width: 200px; text-align: center; }
  .value svg { display: block; margin: 0 auto; height: 48px; }
  .value h3 { margin-top: 16px; font-family: "PT Sans", sans-serif; font-style: italic; font-weight: 400; font-size: 25px; color: var(--ink-soft); }
  .value p { margin-top: 8px; font-size: 11.5px; line-height: 16px; color: var(--ink); }

  .band { left: 24px; top: 827px; width: 1146px; height: 73px; background: var(--band); }
  .band-text { left: 86px; top: 846px; font-family: "PT Sans", sans-serif; font-style: italic; font-size: 25px; color: var(--ink); }
  .band-text em { color: var(--brand); font-style: italic; }
  .strip { top: 896px; height: 4px; background: linear-gradient(90deg, #3d6aa8, #b8c8dc); }
</style>
</head>
<body>
  <div class="page"></div>

  <div class="abs logo">Vorenix</div>

  <div class="abs contact contact-phone">
    <svg width="14" height="12" viewBox="0 0 14 12"><path d="M1 3c0-2 12-2 12 0v2h-3V3.5H4V5H1z"/><rect x="3" y="6" width="8" height="5" rx="1"/></svg>
    02-555-0142
  </div>
  <div class="abs contact contact-mail">
    <svg width="16" height="11" viewBox="0 0 16 11"><rect width="16" height="11" rx="1"/><path d="M1 1l7 5 7-5" stroke="#fff" stroke-width="1.2" fill="none"/></svg>
    info@vorenix-example.com
  </div>

  <nav class="abs nav">
    <a class="active" href="#">Home</a>
    <a href="#" style="width:142px">Services</a>
    <a href="#" style="width:104px">Our Expertise</a>
    <a href="#" style="width:134px">Jobs</a>
    <a href="#" style="width:74px">About Us</a>
    <a href="#" style="width:160px">Contact Us</a>
  </nav>

  <div class="abs hero" role="img" aria-label="Photo of a consultant presenting an org chart on a flip board to a seated team"></div>
  <div class="abs hero-shadow" style="left:90px"></div>
  <div class="abs hero-shadow" style="left:680px"></div>
  <div class="abs tagline"><span class="rule"></span>Your Most Trusted IT Advisor<span class="rule" style="width:38px"></span></div>
  <a class="abs btn">know more</a>

  <h2 class="abs section-title" style="font-weight:400"><span class="rule"></span>Our Values &amp; Services<span class="rule"></span></h2>

  <div class="abs value" style="left:58px">
    <svg viewBox="0 0 56 40" width="56" fill="var(--icon)"><path d="M2 8h12l16 20h10v-7l12 10-12 10v-7H27L11 14H2z"/><path d="M2 28h9l5-6 4 5-6 7H2z"/><path d="M27 12h13V5l12 10-12 10v-7H30l-3 4-4-5z"/></svg>
    <h3>Fast</h3>
    <p>Lorem ipsum dolor sit amet<br>consectetur adipiscing</p>
  </div>

  <div class="abs value" style="left:270px">
    <svg viewBox="0 0 50 44" width="50" fill="none" stroke="var(--icon)" stroke-width="6"><path d="M22 8H4v33h37V30"/><path d="M12 32c2-12 10-17 24-17" /><path d="M34 4l11 11-11 11" fill="var(--icon)" stroke="none" transform="translate(0 0)"/></svg>
    <h3>High Quality</h3>
    <p>Lorem ipsum dolor sit amet<br>consectetur adipiscing</p>
  </div>

  <div class="abs value" style="left:498px">
    <svg viewBox="0 0 56 46" width="56" fill="var(--icon)"><path d="M6 38l24-24 6 6-24 24z"/><path d="M24 4l10-2 8 8-6 6-4-4-4 4-6-6 4-4z"/><path d="M30 28l8-8 14 14c2 2 2 6 0 8s-6 2-8 0z"/><path d="M14 6a8 8 0 0 1 10 10l-4 4-8-8z"/></svg>
    <h3>Services</h3>
    <p>Lorem ipsum dolor sit amet<br>consectetur adipiscing</p>
  </div>

  <div class="abs value" style="left:728px">
    <svg viewBox="0 0 48 40" width="48" fill="var(--icon)"><rect x="2" y="4" width="7" height="7"/><rect x="14" y="5" width="32" height="5"/><rect x="2" y="16" width="7" height="7"/><rect x="14" y="17" width="32" height="5"/><rect x="2" y="28" width="7" height="7"/><rect x="14" y="29" width="32" height="5"/></svg>
    <h3>Customised</h3>
    <p>Lorem ipsum dolor sit amet<br>consectetur adipiscing</p>
  </div>

  <div class="abs value" style="left:936px">
    <svg viewBox="0 0 52 46" width="52" fill="none" stroke="var(--icon)" stroke-width="5"><path d="M30 5H6v24"/><rect x="16" y="15" width="31" height="27" rx="2"/></svg>
    <h3>Customer focus</h3>
    <p>Lorem ipsum dolor sit amet<br>consectetur adipiscing</p>
  </div>

  <div class="abs band"></div>
  <p class="abs band-text">Experienced, certified professionals provide <em>IT consulting</em> by industry recommended practices.</p>
  <div class="abs strip" role="img" aria-label="Row of team photos" style="left:86px;width:323px"></div>
  <div class="abs strip" role="img" aria-label="Team photo" style="left:435px;width:320px"></div>
  <div class="abs strip" role="img" aria-label="Team photo" style="left:785px;width:323px"></div>
</body>
</html>
```